A website for a green bio-plastics manufacturing company

We need a home page designed and two complimentary template pages that can be used for the rest of the website. The template page should vary in design from the home page, but should flow uniformly with it.

This is a very innovative company with a proprietary manufacturing method of using bird feathers to make plastic.

The site should be functional, informative, user-friendly and informative to both our business partners and the consumers.
Updates

I've added a more concise overview of the company.  If any of the designers have any questions for me, please ask.  Thanks

Felix

Target Market(s)

Business partners interested in using bio-plastics for their products and general customers.

Industry/Entity Type

Manufacturing

Number of Pages Required

3 pages

Requirements
Must have
• I attached some information about the company, so the site should be designed to incorporate that content.

Will need to be edited by Adobe Contribute.

Easy to navigate

One of the template pages should have one column for content. The other should have two columns. I''m open to different ideas though.

Should be very pleasing to the eye and uncluttered.

Want to be informative to both our business partners as well as consumers who may be researching our product(s)

Easy to Maintain

Anticipated Tabs/Pages
· Home Page
o General “welcome” page

· About Us
o Company overview and information

· Products
o Horticulture Containers
o Agriculture Films
o Where to Buy
o Upcoming Products

· Business Partners

· Press Releases

· Contact Us

Nice to have
• Would like to have earth tones and or nice greens in the color scheme. They make use of bird feathers for their manufacturing process, so perhaps a real sharp image of a feather can be incorporated into the design. Be creative though.

Perhaps a jQuery nav bar, but that may be out of scope.

Should not have
• No flash at all.

```html
<!DOCTYPE html>
<html lang="en">
<head>
<meta charset="utf-8">
<title>Verdant Polymers — Global Solutions for Bioplastics</title>
<link rel="stylesheet" href="https://fonts.googleapis.com/css2?family=Jost:wght@300;400;500;600&family=Questrial&family=Arimo:wght@400;700&display=swap">
<style>
  :root {
    --white: #ffffff;
    --page-tint: #eaf7e6;
    --footer-tint: #dcebd7;
    --nav-top: #4a4d4a;
    --nav-bottom: #0e0f0e;
    --nav-text: #f2f2f2;
    --leaf: #5e9e1a;
    --leaf-deep: #2f7a24;
    --slate: #8fa2ad;
    --slate-dark: #55666f;
    --ink: #2b2b2b;
    --muted: #777d7a;
    --link: #2a68c4;
    --accent-blue: #3b82c6;
    --rule: #c8d9c4;
    --panel-top: #ffffff;
    --panel-bottom: #e6e9ec;
  }
  * { box-sizing: border-box; margin: 0; padding: 0; }
  html, body { width: 1094px; height: 1200px; overflow: hidden; }
  body {
    position: relative;
    background: var(--white);
    font-family: "Arimo", Arial, sans-serif;
    color: var(--ink);
  }
  a { color: var(--link); }

  .top-rule { position: absolute; left: 0; top: 0; width: 1094px; height: 5px;
    border-top: 2px solid #d0d0d0; border-bottom: 1px solid #e4e4e4; }

  /* header */
  .header-art { position: absolute; left: 378px; top: 29px; width: 193px; height: 114px; z-index: 0;
    background: radial-gradient(ellipse at 45% 45%, #e6e8e8 0%, #f4f5f5 50%, #ffffff 75%); }
  .brand { position: absolute; left: 70px; top: 46px; display: flex; align-items: center; gap: 14px; z-index: 1; }
  .brand-dot { width: 66px; height: 66px; border-radius: 50%; background: var(--leaf-deep); flex: none; }
  .brand-name { font-family: "Questrial", sans-serif; font-size: 33px; color: #3d3d3d; line-height: 34px; letter-spacing: 0.5px; }
  .brand-name span { display: block; white-space: nowrap; }
  .utility { position: absolute; top: 60px; left: 858px; display: flex; gap: 36px; }
  .utility svg { width: 20px; height: 18px; }

  /* navigation */
  .nav-band { position: absolute; left: 0; top: 143px; width: 1094px; height: 118px;
    background: linear-gradient(to bottom, var(--nav-top) 0%, #2a2c2a 45%, var(--nav-bottom) 100%); }
  .nav { position: absolute; left: 0; top: 143px; width: 1094px; height: 56px; list-style: none; }
  .nav li { position: absolute; top: 0; height: 56px; line-height: 56px; text-align: center; white-space: nowrap;
    font-family: "Questrial", sans-serif; font-size: 18px; color: var(--nav-text); letter-spacing: 0; }
  .nav li.current { left: 63px; width: 143px; height: 54px; line-height: 54px; background: var(--white);
    border-radius: 0 0 8px 8px; color: var(--leaf); }
  .nav .sep { position: absolute; top: 2px; width: 1px; height: 52px; background: #151515; box-shadow: 1px 0 0 #5b5e5b; }

  /* hero */
  .hero { position: absolute; left: 36px; top: 210px; width: 1024px; height: 333px; border-radius: 16px 16px 0 0;
    overflow: hidden; background: radial-gradient(ellipse at 20% 48%, #e9ffe2 0%, #62c24a 22%, #2f8d2c 45%, #8fd07d 70%, #d9f2cf 100%); }
  .hero-title { position: absolute; right: 38px; top: 92px; text-align: left; color: var(--white); font-family: "Jost", sans-serif; }
  .hero-title .l1 { display: block; font-weight: 300; font-size: 78px; line-height: 70px; letter-spacing: -2px; }
  .hero-title .l2 { display: block; font-weight: 600; font-size: 30px; line-height: 30px; padding-left: 68px; }
  .hero-title .l3 { display: block; font-weight: 300; font-size: 62px; line-height: 58px; padding-left: 66px; letter-spacing: -1px; }

  .page-tint { position: absolute; left: 0; top: 543px; width: 1094px; height: 550px; background: var(--page-tint); }

  /* features panel */
  .features { position: absolute; left: 36px; top: 543px; width: 1024px; height: 221px; border-radius: 0 0 16px 16px;
    background: linear-gradient(to bottom, var(--panel-top) 30%, var(--panel-bottom) 100%);
    border-top: 1px solid #c6c6c6; box-shadow: 0 2px 4px rgba(0,0,0,0.22); }
  .features .divider { position: absolute; left: 508px; top: 14px; width: 2px; height: 190px; background: #d3d6d8; }
  .feature { position: absolute; top: 0; width: 500px; height: 221px; }
  .feature-art { position: absolute; }
  .feature h2 { position: absolute; font-family: "Jost", sans-serif; font-weight: 500; color: var(--slate);
    font-size: 33px; line-height: 30px; }
  .feature h2 small { display: block; font-size: 18px; line-height: 18px; color: var(--slate-dark); font-weight: 500; }
  .feature p { position: absolute; font-size: 13px; line-height: 19px; color: #222; width: 272px; letter-spacing: 0.3px; }
  .more { position: absolute; font-size: 13.5px; color: #333; white-space: nowrap; }

  /* columns */
  .section-title { position: absolute; font-family: "Jost", sans-serif; font-size: 31px; line-height: 28px; font-weight: 400; color: var(--slate); }
  .section-title strong { color: var(--accent-blue); font-weight: 600; }
  .section-title small { display: block; font-size: 15px; line-height: 16px; color: var(--slate-dark); font-weight: 500; }
  .profile { position: absolute; left: 71px; top: 877px; width: 450px; font-size: 14px; line-height: 20.5px; color: #222; }
  .profile p + p { margin-top: 21px; }
  .services { position: absolute; left: 573px; top: 857px; width: 447px; list-style: none; }
  .services li { height: 32.5px; line-height: 31px; border-bottom: 1px solid var(--rule); font-size: 14px; color: #555; white-space: nowrap; padding-left: 6px; }
  .services .arrow { color: var(--link); font-size: 12px; margin-right: 4px; }
  .services .date { color: var(--link); }

  /* footer */
  .footer { position: absolute; left: 0; top: 1093px; width: 1094px; height: 107px; background: var(--footer-tint); border-top: 2px solid #c9dbc4; }
  .footer .copy { position: absolute; left: 66px; top: 45px; font-size: 12.5px; color: var(--muted); letter-spacing: 0.6px; }
  .footer .legal { position: absolute; right: 71px; top: 45px; font-size: 12.5px; color: var(--muted); letter-spacing: 0.6px; }
  .footer .legal a { color: var(--muted); }
</style>
</head>
<body>
  <div class="top-rule"></div>

  <header>
    <div class="header-art" role="img" aria-label="Soft white feather"></div>
    <div class="brand"><span class="brand-dot"></span><span class="brand-name"><span>Verdant</span><span>Polymers</span></span></div>
    <div class="utility">
      <svg viewBox="0 0 20 18" aria-label="Home"><path d="M3 9 L10 3 L17 9 M5 8 V15 H15 V8" fill="none" stroke="#333" stroke-width="1.6"/><rect x="8.5" y="10.5" width="3" height="4.5" fill="#333"/></svg>
      <svg viewBox="0 0 20 18" aria-label="Site map"><g fill="none" stroke="#555" stroke-width="1.3"><rect x="8" y="2" width="4" height="3"/><rect x="2" y="12" width="4" height="3"/><rect x="8" y="12" width="4" height="3"/><rect x="14" y="12" width="4" height="3"/><path d="M10 5 V9 M4 12 V9 H16 V12 M10 9 V12"/></g></svg>
      <svg viewBox="0 0 20 18" aria-label="Email"><g fill="none" stroke="#555" stroke-width="1.3"><rect x="3" y="5" width="14" height="10"/><path d="M3 5 L10 11 L17 5"/></g></svg>
    </div>
  </header>

  <div class="nav-band"></div>
  <ul class="nav">
    <li class="current">ABOUT US</li>
    <li style="left:236px;width:195px">PRODUCTS</li>
    <li style="left:431px;width:216px">BUSINESS PARTNERS</li>
    <li style="left:647px;width:193px">PRESS RELEASES</li>
    <li style="left:840px;width:214px">CONTACTS</li>
    <span class="sep" style="left:236px"></span>
    <span class="sep" style="left:431px"></span>
    <span class="sep" style="left:647px"></span>
    <span class="sep" style="left:840px"></span>
  </ul>

  <section class="hero" role="img" aria-label="Glowing green glass globe among soft green feathers">
    <h1 class="hero-title"><span class="l1">GLOBAL</span><span class="l2">SOLUTIONS FOR</span><span class="l3">BIOPLASTICS</span></h1>
  </section>

  <div class="page-tint"></div>

  <section class="features">
    <div class="feature" style="left:0">
      <div class="feature-art" role="img" aria-label="Colourful bioplastic cutlery" style="left:17px;top:28px;width:143px;height:132px;background:linear-gradient(90deg,#f4e04a,#f06a3a 30%,#e93d8e 55%,#7fd04a 75%,#f2d23a)"></div>
      <h2 style="left:171px;top:30px">HEADLINE<small>HEADLINE</small></h2>
      <p style="left:171px;top:90px">Aenean bibendum. Cum sociis natoque penatibus et magnis dis parturient montes, nascetur ridiculus mus. Mauris pretium tortor eu dui. Aliquam lectus.</p>
      <span class="more" style="left:344px;top:174px"><a href="#">learn more</a> &gt;&gt;</span>
    </div>
    <div class="divider"></div>
    <div class="feature" style="left:510px">
      <div class="feature-art" role="img" aria-label="White feather with reflection" style="left:8px;top:26px;width:150px;height:131px;background:radial-gradient(ellipse at 45% 40%,#c9cdcf 0%,#e8eaeb 45%,rgba(255,255,255,0) 75%)"></div>
      <h2 style="left:167px;top:30px">MARKETING<small>RESEARCH</small></h2>
      <p style="left:167px;top:90px">Aliquam lectus. quam, scelerisque nec, suscipit in, ornare eget, massa. Maecenas nunc. Vestibulum pede ipsum, hendrerit at, sodales sed, pellentesque quis, mauris.</p>
      <span class="more" style="left:388px;top:174px"><a href="#">learn more</a> &gt;&gt;</span>
    </div>
  </section>

  <section>
    <h2 class="section-title" style="left:71px;top:793px"><strong>WHO</strong> WE ARE<small>COMPANY PROFILE OVERVIEW</small></h2>
    <div class="profile">
      <p>Integer pede nisi, adipng eget, gravida sagittis, placerat vel. Sed a us id <a href="#">nisi feugiat</a> convallis. Vivamus telluse urna, tincidunt vel, commodo sit amet, viverra vitae, enim. Donec vitae odio.</p>
      <p>Nam dictum lorem, tincidunt vel, <a href="#">commodo sit amet</a>, viverra ec vitae odio. Vivamus ut turpis. Cras arcu. tortor. Sed lesuada isse porttitor, mi id tincidunt tristique, nulla nisi feugiat libero. male-</p>
    </div>
    <span class="more" style="left:401px;top:1042px"><a href="#">more about us</a> <a href="#" style="text-decoration:none">&gt;&gt;</a></span>
  </section>

  <section>
    <h2 class="section-title" style="left:573px;top:793px"><strong>WHAT</strong> WE DO<small>FEATURED SERVICES</small></h2>
    <ul class="services">
      <li><span class="arrow">&#8594;</span><span class="date">2007-06-10</span> / Lorem ipsum dolor sit amet consectetuer adipis</li>
      <li><span class="arrow">&#8594;</span><span class="date">2007-06-12</span> / Consectetuer adipiscing elit hasellus sapien</li>
      <li><span class="arrow">&#8594;</span><span class="date">2007-06-10</span> / Lorem ipsum dolor sit amet consectetuer adipi</li>
      <li><span class="arrow">&#8594;</span><span class="date">2007-06-12</span> / Phasellus sapien tortor, fringilla vel, pretium</li>
      <li><span class="arrow">&#8594;</span><span class="date">2007-06-12</span> / Nulla mi urna, faucibus eget, faucibus idodo</li>
    </ul>
    <span class="more" style="left:916px;top:1042px"><a href="#">all services</a> <a href="#" style="text-decoration:none">&gt;&gt;</a></span>
  </section>

  <footer class="footer">
    <span class="copy">Verdant Polymers 2010. All rights reserved</span>
    <span class="legal"><a href="#">Privacy Policy</a> &nbsp;and&nbsp; <a href="#">Terms of Use</a></span>
  </footer>
</body>
</html>
```